Real Estate Open House A Frame Sign

The sign is 22" wide and 28" tall. This sign is used to post around the neighbourhood to direct people to an open house (home that is for sale). It is also used for self-promotion.

Designwise
- I just want something with a modern look, simple and clean.
- I want my picture and business logo on the left side.
- On the right side, website (www.lumwick-realestate.com) and my phone (555-374-9126), then a blank space where I can write an address when I need to.

I'm not sure how I want the overall design look. I'm very open-minded and I'm depending on your creative mind to come up with something.

If you have any questions, please let me know.

```html
<!DOCTYPE html>
<html lang="en">
<head>
<meta charset="utf-8">
<title>Lumwick Real Estate – Open House Sign</title>
<link rel="stylesheet" href="https://fonts.googleapis.com/css2?family=Anton&family=Open+Sans:wght@400;700;800&display=swap">
<style>
  :root {
    --brand-blue: #064187;
    --brand-blue-light: #1a5aa6;
    --ink: #161616;
    --white: #ffffff;
    --photo-dark: #2b2f36;
    --photo-light: #8a8f98;
  }
  * { margin: 0; padding: 0; box-sizing: border-box; }
  html, body {
    width: 960px; height: 1200px; overflow: hidden; background: var(--white);
  }
  .sign {
    position: relative; width: 960px; height: 1200px; overflow: hidden;
    background: var(--white);
    font-family: "Open Sans", Arial, sans-serif;
  }
  .sign-shapes { position: absolute; inset: 0; }
  .brand-name {
    position: absolute; left: 89px; top: 108px;
    font-family: "Open Sans", Arial, sans-serif; font-weight: 700;
    font-size: 38px; line-height: 1; color: var(--white);
    white-space: nowrap;
  }
  .agent-photo {
    position: absolute; left: 50px; top: 298px; width: 440px; height: 636px;
    background: linear-gradient(180deg, var(--photo-light) 0%, var(--photo-dark) 55%, #1f2228 100%);
    border-radius: 200px 200px 0 0;
  }
  .headline {
    position: absolute; right: 62px; top: 318px; text-align: right;
    font-family: "Anton", Impact, sans-serif; line-height: 0.92;
  }
  .headline-open {
    display: block; font-size: 196px; letter-spacing: -2px;
    background: linear-gradient(180deg, #6a6a6a 0%, #111 45%, #000 100%);
    -webkit-background-clip: text; background-clip: text; color: transparent;
  }
  .headline-house {
    display: block; font-size: 154px;
    background: linear-gradient(180deg, var(--brand-blue-light) 0%, var(--brand-blue) 60%, #03306a 100%);
    -webkit-background-clip: text; background-clip: text; color: transparent;
    margin-top: 14px;
  }
  .contact { position: absolute; right: 62px; top: 852px; text-align: right; color: var(--white); }
  .contact-web { font-size: 31px; font-weight: 400; white-space: nowrap; }
  .contact-web strong { font-weight: 700; }
  .contact-phone { font-size: 66px; font-weight: 800; letter-spacing: 1px; margin-top: 4px; line-height: 1.1; white-space: nowrap; }
  .address {
    position: absolute; left: 0; right: 0; top: 1060px; text-align center;
    text-align: center; color: var(--white); font-size: 63px; font-weight: 800;
    letter-spacing: 1px; line-height: 1.1; white-space: nowrap;
  }
</style>
</head>
<body>
<main class="sign">
  <svg class="sign-shapes" viewBox="0 0 960 1200" width="960" height="1200" aria-hidden="true">
    <path class="top-swoosh" fill="var(--ink)"
      d="M0 0 H960 V170 C860 115 750 135 630 205 C540 255 470 282 400 290 Z"/>
    <path class="top-band" fill="var(--brand-blue)"
      d="M0 0 H960 V100 C860 60 740 80 620 150 C500 220 420 290 260 272 C150 258 60 225 0 200 Z"/>
  </svg>

  <div class="brand-name">LUMWICK REAL ESTATE</div>

  <div class="headline">
    <span class="headline-open">OPEN</span>
    <span class="headline-house">HOUSE</span>
  </div>

  <div class="agent-photo" role="img" aria-label="Portrait photo of the agent in a dark suit with arms crossed"></div>

  <svg class="sign-shapes" viewBox="0 0 960 1200" width="960" height="1200" aria-hidden="true">
    <path class="bottom-band" fill="var(--brand-blue)"
      d="M0 885 C80 930 160 948 260 938 C420 918 520 752 700 745 C820 742 900 780 960 800 V1020 H0 Z"/>
    <rect class="address-band" x="0" y="1015" width="960" height="185" fill="var(--ink)"/>
  </svg>

  <div class="agent-photo" role="img" aria-label="Lower part of the agent portrait overlapping the blue band"
       style="clip-path: inset(580px 0 0 0);"></div>

  <div class="contact">
    <div class="contact-web">www.<strong>lumwick-realestate</strong>.com</div>
    <div class="contact-phone">555-374-9126</div>
  </div>

  <div class="address">LOREM IPSUM ADDRESS</div>
</main>
</body>
</html>
```